Business Card Design

We need a basic, but modern design card. Our business is a local Queanbeyan/Canberra courier service, but can organise interstate delivery if needed. Our fleet ranges from 1 tonne vans to 8 tonne trucks.

Industry/Entity Type

Business

Contact Information for Business Card

Harbourline Freight
14 Tarrant Road
Karrawong NSW 2631

Owen Prescott
CEO

Phone: 02 61847315
Fax: 02 61847398
email: owen@harbourlinefreight.com.au

```html
<!DOCTYPE html>
<html lang="en">
<head>
<meta charset="utf-8">
<title>Harbourline Freight – Business Card</title>
<link rel="stylesheet" href="https://fonts.googleapis.com/css2?family=Arimo:wght@400;700&display=swap">
<style>
  :root {
    --backdrop: #e9e7e3;
    --card-stock: #f1f0ec;
    --ink: #2b2b2b;
    --brand-blue: #1b74bf;
    --brand-yellow: #f7b21b;
  }
  * { box-sizing: border-box; margin: 0; padding: 0; }
  html, body {
    width: 1200px;
    height: 1000px;
    overflow: hidden;
    background: var(--backdrop);
    font-family: "Arimo", Arial, sans-serif;
  }
  .stage {
    position: relative;
    width: 1200px;
    height: 1000px;
  }
  .business-card {
    position: absolute;
    left: 150px;
    top: 225px;
    width: 900px;
    height: 550px;
    background: var(--card-stock);
    box-shadow: 0 10px 30px rgba(0,0,0,0.12);
    overflow: hidden;
  }
  .card-holder {
    position: absolute;
    top: 66px;
    left: 545px;
    font-size: 21px;
    line-height: 1.3;
    color: var(--ink);
    white-space: nowrap;
  }
  .brand {
    position: absolute;
    left: 105px;
    top: 190px;
    display: flex;
    align-items: center;
    gap: 18px;
  }
  .brand-square {
    width: 46px;
    height: 46px;
    background: var(--brand-yellow);
    flex: none;
  }
  .brand-name {
    font-size: 40px;
    font-weight: 700;
    line-height: 1.05;
    color: var(--brand-blue);
    width: 260px;
  }
  .contact-details {
    position: absolute;
    left: 465px;
    top: 262px;
    font-size: 21px;
    line-height: 1.3;
    color: var(--ink);
    list-style: none;
    white-space: nowrap;
  }
  .contact-details .indent { padding-left: 8px; }
  .edge-band {
    position: absolute;
    left: 0;
    bottom: 0;
    width: 100%;
    height: 16px;
    display: flex;
  }
  .edge-band .band-yellow { flex: 1; background: var(--brand-yellow); }
  .edge-band .band-blue { width: 52px; background: var(--brand-blue); }
</style>
</head>
<body>
  <main class="stage">
    <article class="business-card">
      <p class="card-holder">Owen Prescott CEO</p>
      <div class="brand">
        <span class="brand-square" aria-hidden="true"></span>
        <span class="brand-name">Harbourline Freight</span>
      </div>
      <ul class="contact-details">
        <li class="indent">14 Tarrant Road</li>
        <li class="indent">Karrawong NSW 2631</li>
        <li>Phone: 02 61847315</li>
        <li>Fax: 02 61847398</li>
        <li>email: owen@harbourlinefreight.com.au</li>
      </ul>
      <div class="edge-band" aria-hidden="true">
        <span class="band-yellow"></span>
        <span class="band-blue"></span>
      </div>
    </article>
  </main>
</body>
</html>
```